Bramblecrest Roofing Co. business card design

I am a Roofing contractor in Texas. The name of my company is Bramblecrest Roofing Co. I also offer a few other services (Christmas light installation, gutters, fencing, pressure washing). However my main gig is roofing. Storm restoration and knowledge of the insurance claim process is my specialty.

My colors are black, red and white. I’d like something pretty simple and clean. Modern looking but with a splash of this red tartan pattern.

I have another version of my logo being edited at the moment where the little top part of the F in roofing that’s currently tartan will be changed to just solid red to make it more visible. So if that’s something you can change in your mock up great. But I can provide the full version once the contest is complete

Target Market(s)

Homeowners

Industry/Entity Type

Roofing

Contact Information for Business Card

Darren Pike. 682-555-0193. www.bramblecrest roofing.example Darren@bramblecrestroofing.example

Colors
EB3D1F
EC4F4E
F09395
F8D3D4
FCEDEE

Requirements
Nice to have
• Maybe instead of a business address. I could say serving all DFW Texas or something like that. And maybe add a line somewhere saying deductible assistance? Just a thought

```html
<!DOCTYPE html>
<html lang="en">
<head>
<meta charset="UTF-8">
<title>Bramblecrest Roofing Co. – Business Card</title>
<link href="https://fonts.googleapis.com/css2?family=Montserrat:wght@400;500;700;800&display=swap" rel="stylesheet">
<style>
  :root {
    --page-bg: #e4e4e4;
    --card-bg: #232323;
    --brand-red: #d3302a;
    --ink-white: #ffffff;
    --ink-soft: #f1f1f1;
  }
  * { box-sizing: border-box; margin: 0; padding: 0; }
  html, body {
    width: 1200px; height: 1200px; overflow: hidden;
    background: var(--page-bg);
    font-family: "Montserrat", sans-serif;
  }
  .canvas {
    width: 1200px; height: 1200px;
    display: flex; justify-content: center; align-items: center; gap: 60px;
  }
  .card {
    width: 480px; height: 800px;
    background: var(--card-bg);
    border-radius: 26px;
    box-shadow: 0 18px 40px rgba(0,0,0,0.25);
    display: flex; flex-direction: column; align-items: center;
    position: relative;
    color: var(--ink-white);
  }
  .brand-mark {
    width: 170px; height: 170px; border-radius: 50%;
    background: var(--brand-red);
    border: 6px solid var(--ink-white);
  }
  .brand-name {
    margin-top: 22px;
    font-weight: 800; font-size: 40px; line-height: 1.08;
    text-transform: uppercase; letter-spacing: 2px;
    color: var(--brand-red); text-align: center;
  }
  .card--front .brand-mark { margin-top: 80px; }
  .person { margin-top: 70px; text-align: center; }
  .person-name {
    font-weight: 700; font-size: 32px; letter-spacing: 2px;
    color: var(--brand-red); text-transform: uppercase;
  }
  .person-title { font-weight: 500; font-size: 21px; margin-top: 2px; }
  .divider {
    margin-top: 42px; width: 360px;
    display: flex; align-items: center; gap: 10px;
  }
  .divider-line { flex: 1; height: 1.5px; background: var(--brand-red); }
  .contact-icon {
    width: 26px; height: 26px; border-radius: 4px;
    background: var(--brand-red);
    display: flex; align-items: center; justify-content: center;
  }
  .contact-list {
    list-style: none; margin-top: 20px; text-align: center;
    font-size: 19px; line-height: 1.55; color: var(--ink-soft);
  }
  .card--back .brand-mark { margin-top: 200px; }
  .service-area {
    position: absolute; bottom: 90px;
    font-weight: 500; font-size: 24px; letter-spacing: 1px;
  }
</style>
</head>
<body>
<main class="canvas">
  <section class="card card--front">
    <div class="brand-mark"></div>
    <h1 class="brand-name">Bramblecrest<br>Roofing Co.</h1>
    <div class="person">
      <p class="person-name">Darren Pike</p>
      <p class="person-title">CEO/Founder</p>
    </div>
    <div class="divider">
      <span class="divider-line"></span>
      <span class="contact-icon">
        <svg width="16" height="16" viewBox="0 0 24 24" fill="#fff"><path d="M6.6 10.8a15 15 0 0 0 6.6 6.6l2.2-2.2c.3-.3.7-.4 1-.2 1.1.4 2.3.6 3.6.6.6 0 1 .4 1 1V20c0 .6-.4 1-1 1A17 17 0 0 1 3 4c0-.6.4-1 1-1h3.5c.6 0 1 .4 1 1 0 1.3.2 2.5.6 3.6.1.3 0 .7-.2 1l-2.3 2.2z"/></svg>
      </span>
      <span class="contact-icon">
        <svg width="16" height="16" viewBox="0 0 24 24" fill="none" stroke="#fff" stroke-width="2"><rect x="3" y="5" width="18" height="14" rx="1"/><path d="M3 6l9 7 9-7"/></svg>
      </span>
      <span class="contact-icon">
        <svg width="16" height="16" viewBox="0 0 24 24" fill="none" stroke="#fff" stroke-width="1.8"><circle cx="12" cy="12" r="9"/><path d="M3 12h18M12 3c3 3 3 15 0 18M12 3c-3 3-3 15 0 18"/></svg>
      </span>
      <span class="divider-line"></span>
    </div>
    <ul class="contact-list">
      <li>682-555-0193</li>
      <li>Darren@bramblecrestroofing.example</li>
      <li>www.bramblecrest roofing.example</li>
    </ul>
  </section>

  <section class="card card--back">
    <div class="brand-mark"></div>
    <h2 class="brand-name">Bramblecrest<br>Roofing Co.</h2>
    <p class="service-area">Serving all DFW Texas</p>
  </section>
</main>
</body>
</html>
```